Bref créative
Business Cards & Satationary for Copperfield Homes
Dallin Marsh
Professional
Copperfield Homes
PO Box 587
KELMORE RISE Q 4390
M: 0417 562 908
info@copperfieldhomes.com.au
www.copperfieldhomes.com.au
NHRA Licence No. 80394. Housing Registry Office of Tasmania No. HR-K61402
Residential Construction
"Builder of Quality not Quantity"
E:info@copperfieldhomes.com.au

```html
<!DOCTYPE html>
<html lang="en">
<head>
<meta charset="utf-8">
<title>Copperfield Homes – Business Cards</title>
<link rel="stylesheet" href="https://fonts.googleapis.com/css2?family=Open+Sans:wght@400;600;700&display=swap">
<style>
  :root {
    --copper: #d4532b;
    --copper-deep: #c2461f;
    --paper: #ffffff;
    --backdrop: #ece8e3;
    --ink: #555555;
    --ink-soft: #7a7a7a;
  }
  html, body {
    margin: 0;
    padding: 0;
    overflow: hidden;
  }
  body {
    width: 1200px;
    height: 629px;
    background: var(--backdrop);
    font-family: "Open Sans", Arial, sans-serif;
    position: relative;
  }
  .card {
    position: absolute;
    top: 170px;
    width: 500px;
    height: 286px;
    box-shadow: 0 6px 18px rgba(0,0,0,0.18);
    box-sizing: border-box;
  }
  .card--front {
    left: 70px;
    background: linear-gradient(135deg, var(--copper) 0%, var(--copper-deep) 100%);
    display: flex;
    align-items: center;
    justify-content: center;
  }
  .card--back {
    left: 630px;
    background: var(--paper);
  }
  .brand {
    display: flex;
    align-items: center;
    gap: 12px;
  }
  .brand__mark {
    width: 34px;
    height: 34px;
    background: var(--paper);
  }
  .brand__name {
    font-weight: 600;
    font-size: 24px;
    letter-spacing: 2px;
    text-transform: uppercase;
    color: var(--paper);
  }
  .card--back .brand {
    position: absolute;
    left: 34px;
    top: 40px;
    gap: 9px;
  }
  .card--back .brand__mark {
    width: 24px;
    height: 24px;
    background: var(--copper);
  }
  .card--back .brand__name {
    font-size: 17px;
    letter-spacing: 1.5px;
    color: var(--copper);
  }
  .contact {
    position: absolute;
    left: 34px;
    top: 128px;
  }
  .contact__name {
    font-size: 14px;
    font-weight: 700;
    color: var(--copper);
    margin: 0 0 10px;
  }
  .contact__list {
    list-style: none;
    margin: 0;
    padding: 0;
  }
  .contact__item {
    display: flex;
    align-items: center;
    gap: 8px;
    font-size: 11px;
    color: var(--ink);
    margin-bottom: 6px;
  }
  .contact__icon {
    width: 14px;
    height: 14px;
    flex: none;
  }
  .address {
    position: absolute;
    left: 34px;
    bottom: 26px;
    font-size: 10px;
    color: var(--ink-soft);
    letter-spacing: 0.3px;
  }
</style>
</head>
<body>

<section class="card card--front" aria-label="Business card front">
  <div class="brand">
    <span class="brand__mark"></span>
    <span class="brand__name">Copperfield Homes</span>
  </div>
</section>

<section class="card card--back" aria-label="Business card back">
  <div class="brand">
    <span class="brand__mark"></span>
    <span class="brand__name">Copperfield Homes</span>
  </div>

  <div class="contact">
    <p class="contact__name">Dallin Marsh</p>
    <ul class="contact__list">
      <li class="contact__item">
        <svg class="contact__icon" viewBox="0 0 14 14" aria-hidden="true">
          <circle cx="7" cy="7" r="7" fill="#d4532b"/>
          <path d="M4.6 3.6 L5.8 3.6 L6.3 5.3 L5.5 6 Q6.2 7.6 7.9 8.5 L8.6 7.7 L10.3 8.2 L10.3 9.4 Q9.8 10.3 8.8 10.2 Q4.3 9.4 3.8 4.6 Q3.8 3.8 4.6 3.6 Z" fill="#fff"/>
        </svg>
        M: 0417 562 908
      </li>
      <li class="contact__item">
        <svg class="contact__icon" viewBox="0 0 14 14" aria-hidden="true">
          <circle cx="7" cy="7" r="7" fill="#d4532b"/>
          <rect x="3.5" y="4.5" width="7" height="5" fill="#fff"/>
          <path d="M3.5 4.5 L7 7.3 L10.5 4.5" fill="none" stroke="#d4532b" stroke-width="0.8"/>
        </svg>
        E: info@copperfieldhomes.com.au
      </li>
      <li class="contact__item">
        <svg class="contact__icon" viewBox="0 0 14 14" aria-hidden="true">
          <circle cx="7" cy="7" r="7" fill="#d4532b"/>
          <circle cx="7" cy="7" r="3.6" fill="none" stroke="#fff" stroke-width="0.9"/>
          <ellipse cx="7" cy="7" rx="1.5" ry="3.6" fill="none" stroke="#fff" stroke-width="0.8"/>
          <line x1="3.4" y1="7" x2="10.6" y2="7" stroke="#fff" stroke-width="0.8"/>
        </svg>
        www.copperfieldhomes.com.au
      </li>
    </ul>
  </div>

  <p class="address">PO Box 587, KELMORE RISE Q 4390</p>
</section>

</body>
</html>
```